Business card design needed

We need a buisness card design to suit our buisness "Maple Parcel", a company on the south coast of Australia, a wholesale greeting card and gift wrap buisness. We are open to different colour options possibly some pastels. A card that got my attention was'the ''hoofnotes.com.au'' buisness card. I liked the colour scheme, layout, and the use of a cartoon image, but am also open to all ideas.

Industry/Entity Type

Business

Contact Information for Business Card

Maple Parcel Unit 37 / 18 Banksia ave West Torrin 2563 ph 0244879351 fax 0244879352 Colin Madsey email maple.parcel@postvale.com

```html
<!DOCTYPE html>
<html lang="en">
<head>
<meta charset="utf-8">
<title>Maple Parcel – Business Card</title>
<link rel="stylesheet" href="https://fonts.googleapis.com/css2?family=Arvo:wght@400&family=Sorts+Mill+Goudy&display=swap">
<style>
  :root {
    --paper: #f4f3f8;
    --pattern-lilac: #e3dcec;
    --pattern-blue: #dde8f2;
    --pattern-rose: #eedde6;
    --title-orange: #e2602a;
    --title-shade: #b8441a;
    --band-left: #e7632a;
    --band-light: #f8a653;
    --band-mid: #ef6c2a;
    --band-dark: #a11d24;
    --bow-light: #f9a445;
    --bow-deep: #e86a1c;
    --info-grey: #585858;
  }
  html, body {
    margin: 0;
    padding: 0;
    overflow: hidden;
    background: #ffffff;
  }
  .card {
    position: relative;
    width: 1200px;
    height: 741px;
    overflow: hidden;
    background: var(--paper);
  }
  .floral-backdrop {
    position: absolute;
    inset: 0;
    background:
      radial-gradient(ellipse 70% 22% at 50% 40%, rgba(255,255,255,0.85), rgba(255,255,255,0) 100%),
      radial-gradient(ellipse 80% 40% at 50% 90%, rgba(255,255,255,0.6), rgba(255,255,255,0) 100%),
      linear-gradient(160deg, var(--pattern-lilac) 0%, var(--pattern-blue) 35%, var(--pattern-rose) 65%, var(--pattern-lilac) 100%);
  }
  .brand-title {
    position: absolute;
    left: 0;
    width: 1260px;
    top: 248px;
    margin: 0;
    text-align: center;
    font-family: "Arvo", serif;
    font-weight: 400;
    font-size: 94px;
    line-height: 1;
    letter-spacing: 1px;
    color: var(--title-orange);
    text-shadow: 0 -1px 0 var(--title-shade), 0 2px 2px rgba(255,255,255,0.9);
  }
  .ribbon-band {
    position: absolute;
    left: 0;
    top: 408px;
    width: 1200px;
    height: 81px;
    background: linear-gradient(90deg, var(--band-left) 0%, var(--band-light) 31%, var(--band-mid) 60%, var(--band-dark) 100%);
  }
  .gift-bow {
    position: absolute;
    left: 849px;
    top: 368px;
    width: 262px;
    height: 240px;
  }
  .contact-details {
    position: absolute;
    left: 0;
    width: 1240px;
    top: 649px;
    margin: 0;
    text-align: center;
    font-family: "Sorts Mill Goudy", serif;
    font-size: 20px;
    line-height: 36px;
    color: var(--info-grey);
  }
  .contact-details span {
    display: block;
  }
</style>
</head>
<body>
  <main class="card">
    <div class="floral-backdrop" role="img" aria-label="Soft pastel floral pattern background in lilac, blue and rose"></div>

    <h1 class="brand-title">Maple Parcel</h1>

    <div class="ribbon-band"></div>

    <svg class="gift-bow" viewBox="0 0 262 240" role="img" aria-label="Orange gift ribbon bow with trailing tails">
      <defs>
        <radialGradient id="bowTone" cx="50%" cy="30%" r="70%">
          <stop offset="0%" stop-color="var(--bow-deep)"/>
          <stop offset="100%" stop-color="var(--bow-light)"/>
        </radialGradient>
      </defs>
      <ellipse cx="131" cy="120" rx="128" ry="116" fill="url(#bowTone)" opacity="0.85"/>
    </svg>

    <p class="contact-details">
      <span>Maple Parcel Unit 37 / 18 , Banksia ave West Torrin 2563</span>
      <span>Ph : 0244879351 , fax : 0244879352 , Colin Madsey email maple.parcel@postvale.com</span>
    </p>
  </main>
</body>
</html>
```